North Fern Holdings Business Card

A business card design to accompany the logo design you completed on Artisan Hive. We are open to your proposals. I did add one idea below that might work, but we aren't married to the idea. The company is a real estate services company. Clientele are typically high net worth individuals, executive level employment or owners of their own company, 30-60 years old.

Our 1 (bad?) idea: double sided card; One side landscape with logo and word mark. Other side Portrait with the logo only (oversize watermark maybe?). Somewhere add text of Name (Marcus Pellington), Title (Principal), phone # (949-555-0173) and email address (marcus@northfernhq.com). There would be a second design with my wife's name, number and email in place of mine.

Again totally open to ideas here.

Industry/Entity Type

Real Estate

```html
<!DOCTYPE html>
<html lang="en">
<head>
<meta charset="utf-8">
<title>North Fern Holdings Business Card</title>
<link href="https://fonts.googleapis.com/css2?family=Arimo:wght@400;700&family=Cinzel:wght@400&display=swap" rel="stylesheet">
<style>
  :root {
    --fern-green: #5b9559;
    --fern-green-dark: #4d8a4c;
    --card-white: #ffffff;
    --stage: #ece9e4;
    --ink-grey: #8c8c8c;
  }
  html, body {
    margin: 0;
    width: 1200px;
    height: 1019px;
    overflow: hidden;
    background: var(--stage);
  }
  .stage {
    position: relative;
    width: 1200px;
    height: 1019px;
  }
  .card {
    position: absolute;
    top: 160px;
    width: 400px;
    height: 700px;
    overflow: hidden;
    box-shadow: 0 6px 18px rgba(0,0,0,0.18);
  }
  .card--front { left: 150px; background: var(--fern-green); color: var(--card-white); }
  .card--back { left: 650px; background: var(--card-white); }

  .card__swoosh { position: absolute; left: 0; top: 0; width: 400px; height: 700px; }

  .brand-mark {
    position: absolute;
    left: 0; right: 0;
    text-align: center;
    font-family: "Cinzel", serif;
    font-weight: 400;
  }
  .brand-mark__dot {
    display: block;
    margin: 0 auto 18px;
    border-radius: 50%;
  }
  .card--front .brand-mark { top: 110px; font-size: 24px; color: var(--card-white); letter-spacing: 1px; }
  .card--front .brand-mark__dot { width: 70px; height: 70px; border: 4px solid var(--card-white); box-sizing: border-box; }

  .holder {
    position: absolute;
    left: 44px;
    top: 330px;
    font-family: "Arimo", sans-serif;
  }
  .holder__name { margin: 0; font-size: 26px; font-weight: 700; letter-spacing: 0.5px; }
  .holder__title { margin: 4px 0 0; font-size: 19px; font-weight: 400; }

  .contact {
    position: absolute;
    left: 44px;
    top: 440px;
    margin: 0; padding: 0;
    list-style: none;
    font-family: "Arimo", sans-serif;
    font-size: 19px;
  }
  .contact__item { display: flex; align-items: center; gap: 10px; margin-bottom: 14px; }
  .contact__icon { width: 26px; height: 26px; flex: none; }

  .card--back .brand-mark { top: 230px; color: var(--fern-green); }
  .card--back .brand-mark__dot { width: 60px; height: 60px; background: var(--fern-green); }
  .brand-mark__line { display: block; font-size: 40px; line-height: 1.15; }
</style>
</head>
<body>
<main class="stage">

  <section class="card card--front" aria-label="Business card, contact side">
    <svg class="card__swoosh" viewBox="0 0 400 700" aria-hidden="true">
      <path d="M0,575 C130,600 270,640 400,690 L400,700 L0,700 Z" fill="var(--card-white)"/>
      <path d="M0,600 C140,618 280,656 400,700 L0,700 Z" fill="var(--fern-green)"/>
      <path d="M0,628 C150,642 290,675 360,700 L0,700 Z" fill="var(--card-white)"/>
    </svg>

    <div class="brand-mark">
      <span class="brand-mark__dot"></span>
      North Fern Holdings
    </div>

    <div class="holder">
      <h1 class="holder__name">MARCUS PELLINGTON</h1>
      <p class="holder__title">Principal</p>
    </div>

    <ul class="contact">
      <li class="contact__item">
        <svg class="contact__icon" viewBox="0 0 26 26" aria-hidden="true">
          <circle cx="13" cy="13" r="13" fill="var(--card-white)"/>
          <path d="M9 7 L11.5 7 L12.5 10 L11 11.3 C11.8 13 13 14.2 14.7 15 L16 13.5 L19 14.5 L19 17 C19 18 18 19 17 19 C11.5 18.5 7.5 14.5 7 9 C7 8 8 7 9 7 Z" fill="var(--fern-green)"/>
        </svg>
        <span>949-555-0173</span>
      </li>
      <li class="contact__item">
        <svg class="contact__icon" viewBox="0 0 26 26" aria-hidden="true">
          <circle cx="13" cy="13" r="13" fill="var(--card-white)"/>
          <rect x="6.5" y="8.5" width="13" height="9" fill="var(--fern-green)"/>
          <path d="M6.5 8.5 L13 13.5 L19.5 8.5" fill="none" stroke="var(--card-white)" stroke-width="1.2"/>
        </svg>
        <span>marcus@northfernhq.com</span>
      </li>
    </ul>
  </section>

  <section class="card card--back" aria-label="Business card, brand side">
    <svg class="card__swoosh" viewBox="0 0 400 700" aria-hidden="true">
      <path d="M0,560 C140,575 290,625 400,700 L0,700 Z" fill="var(--fern-green)"/>
      <path d="M0,585 C150,598 270,640 340,700 L325,700 C260,648 140,606 0,592 Z" fill="var(--card-white)"/>
    </svg>

    <div class="brand-mark">
      <span class="brand-mark__dot"></span>
      <span class="brand-mark__line">North Fern</span>
      <span class="brand-mark__line">Holdings</span>
    </div>
  </section>

</main>
</body>
</html>
```